QT Bridgeway Business Card design

I need a business card design based on the logo you did for me.

Some where it should say "Online & Social Media Marketing"

I would like to see how you would do a double sided design. Although I may go with one side and have the other side just a sold color.

Industry/Entity Type

Business

```html
<!DOCTYPE html>
<html lang="en">
<head>
<meta charset="utf-8">
<title>QT Bridgeway Business Card</title>
<link rel="stylesheet" href="https://fonts.googleapis.com/css2?family=Open+Sans:wght@400;600;700&family=Oswald:wght@500;600&family=Saira:wght@400&display=swap">
<style>
  :root {
    --brand-blue: #00aeef;
    --ink: #2b2b2b;
    --muted: #5a5a5a;
    --paper-light: #ffffff;
    --paper-shade: #d4d4d4;
    --white: #ffffff;
    --backdrop: #ecebe8;
  }
  * { margin: 0; padding: 0; box-sizing: border-box; }
  html, body {
    width: 1200px; height: 1019px; overflow: hidden;
    background: var(--backdrop);
  }
  .sheet {
    position: relative; width: 1200px; height: 1019px;
    display: flex; flex-direction: column; align-items: center; justify-content: center; gap: 60px;
  }
  .card {
    position: relative; width: 760px; height: 420px;
    box-shadow: 0 12px 30px rgba(0,0,0,0.18);
    overflow: hidden;
  }
  .card--back { background: var(--brand-blue); height: 380px; width: 760px; }

  .card__identity {
    position: absolute; inset: 0 0 168px 0;
    background: radial-gradient(ellipse at 62% 70%, var(--paper-light) 0%, #f2f2f2 35%, var(--paper-shade) 100%);
  }
  .company {
    position: absolute; left: 40px; bottom: 34px;
  }
  .company__name {
    font-family: "Open Sans", sans-serif; font-weight: 600;
    font-size: 40px; letter-spacing: 2px; color: var(--brand-blue); line-height: 1.1;
  }
  .company__tagline {
    font-family: "Open Sans", sans-serif; font-weight: 400;
    font-size: 19px; color: var(--muted); letter-spacing: 0.4px;
  }
  .person {
    position: absolute; right: 40px; top: 42px; text-align: right;
  }
  .person__name {
    font-family: "Oswald", sans-serif; font-weight: 600;
    font-size: 46px; color: var(--ink); letter-spacing: 1px; line-height: 1;
  }
  .person__title {
    font-family: "Open Sans", sans-serif; font-weight: 400;
    font-size: 17px; color: var(--ink); letter-spacing: 2.5px; margin-top: 6px;
  }

  .card__contact {
    position: absolute; left: 0; right: 0; bottom: 0; height: 168px;
    background: var(--brand-blue);
  }
  .contact__rule { position: absolute; left: 0; top: 22px; }
  .contact__labels {
    position: absolute; top: 8px; left: 0; right: 0; height: 40px;
  }
  .contact__label {
    position: absolute; top: 0;
    font-family: "Oswald", sans-serif; font-weight: 600;
    font-size: 29px; color: var(--white); letter-spacing: 1px; line-height: 40px;
    padding: 0 12px; background: var(--brand-blue);
  }
  .contact__label--address { left: 28px; }
  .contact__label--phone { left: 300px; }
  .contact__label--email { left: 540px; }
  .contact__detail {
    position: absolute; top: 62px;
    font-family: "Saira", sans-serif; font-size: 17px; color: var(--white);
    line-height: 1.45; letter-spacing: 0.8px;
  }
  .contact__detail--address { left: 40px; }
  .contact__detail--phone { left: 312px; }
  .contact__detail--email { left: 552px; }
</style>
</head>
<body>
<main class="sheet">
  <section class="card card--front" aria-label="Business card front">
    <div class="card__identity">
      <div class="person">
        <div class="person__name">DANIEL REYES</div>
        <div class="person__title">GENERAL MANAGER</div>
      </div>
      <div class="company">
        <div class="company__name">QT Bridgeway</div>
        <div class="company__tagline">Online &amp; Social Media Marketing</div>
      </div>
    </div>
    <div class="card__contact">
      <svg class="contact__rule" width="760" height="8" viewBox="0 0 760 8" aria-hidden="true">
        <rect x="0" y="0" width="760" height="7" fill="#ffffff"/>
      </svg>
      <div class="contact__labels">
        <span class="contact__label contact__label--address">ADDRESS</span>
        <span class="contact__label contact__label--phone">PHONE</span>
        <span class="contact__label contact__label--email">EMAIL</span>
      </div>
      <div class="contact__detail contact__detail--address">117 6th floor Plaza<br>Westgate Road NRB</div>
      <div class="contact__detail contact__detail--phone">014 552 7310<br>014 552 7310</div>
      <div class="contact__detail contact__detail--email">hello@qtbridgeway.com<br>www.qtbridgeway.com</div>
    </div>
  </section>
  <section class="card card--back" aria-label="Business card back, solid colour"></section>
</main>
</body>
</html>
```